Business Card for Quillmark Ledger - A cannabis publication for executives.

I'd like some business cards for Quillmark Ledger. The logo is done (great job!) and I need a card design I will use with PRINTLY. I made it a short project to allow time for printing before an event. These will be standard sized cards (final artwork size 3.66" x 2.16" at 300dpi) with a final card size of 3.5" x 2.0". (See PRINTLY.com if you need more info.) I might try rounded corners but am not sure yet. I think the design will work okay with rounded.

Quillmark Ledger will be a bi-weekly publication for the cannabis industry. It is targeted to investors and industry executives, not consumers or pot smokers. So our market is more B2B. However I am open to creativity and making the card something people remark on.

My contact for card:

Dana Merrow
Founder/CEO
dana@quillmarkledger.example

2740 Harlow Avenue
Boston MA 02135
(617)555-0194

Target Market(s)

Executives, Industry people and investors in the Cannabis sector.

Contact Information for Business Card

PRINTLY does do double sided and the second side can be the same or different images. Only one side is required but use of the second side would be a bonus.

Font styles to use
Serif
Sans Serif
Decorative

Colors

Designer to choose colors to be used in the design.

Requirements
Must have
• Logo, contact info
Nice to have
• Style and design to make the card stand out in a crowd.

```html
<!DOCTYPE html>
<html lang="en">
<head>
<meta charset="utf-8">
<title>Quillmark Ledger — Business Card</title>
<link rel="stylesheet" href="https://fonts.googleapis.com/css2?family=Source+Sans+3:wght@400;600;700&family=Roboto+Condensed:wght@300;700&display=swap">
<style>
  :root {
    --stage: #e4e8ea;
    --navy: #232a38;
    --wave-grey: #7a7680;
    --paper: #ffffff;
    --brand-green: #7ab02f;
    --ink-slate: #6c7f85;
    --frame-slate: #6e8288;
  }
  * { box-sizing: border-box; margin: 0; padding: 0; }
  html, body {
    width: 1200px; height: 1000px; overflow: hidden;
    background: var(--stage);
    font-family: "Source Sans 3", Arial, sans-serif;
  }
  .canvas { position: relative; width: 1200px; height: 1000px; }

  .card { position: absolute; background: var(--paper); overflow: hidden; }

  /* Front face */
  .card-front { left: 163px; top: 33px; width: 658px; height: 407px; }
  .card-front .wave-art { position: absolute; inset: 0; width: 100%; height: 100%; }
  .brand {
    position: absolute; left: 0; right: 0; top: 112px;
    display: flex; align-items: center; justify-content: center; gap: 18px;
  }
  .brand-dot { width: 40px; height: 40px; border-radius: 50%; background: var(--brand-green); }
  .brand-name {
    font-family: "Source Sans 3", Arial, sans-serif;
    font-weight: 700; font-size: 56px; line-height: 1;
    color: var(--brand-green); letter-spacing: 0.5px;
  }

  /* Back face */
  .card-back { left: 367px; top: 533px; width: 670px; height: 400px; color: var(--ink-slate); }
  .contact-frame {
    position: absolute; left: 44px; top: 42px; width: 583px; height: 314px;
    border: 4px solid var(--frame-slate); border-radius: 26px;
  }
  .person { position: absolute; left: 0; right: 0; top: 104px; text-align: center; }
  .person-name {
    font-family: "Roboto Condensed", Arial, sans-serif;
    font-size: 29px; letter-spacing: 4px; line-height: 1;
  }
  .person-name .first { font-weight: 300; }
  .person-name .last { font-weight: 700; }
  .person-title { margin-top: 8px; font-size: 17px; }

  .contact-list { position: absolute; left: 142px; top: 226px; list-style: none; }
  .contact-item {
    display: flex; align-items: center; gap: 10px;
    height: 39px; font-size: 18px;
  }
  .contact-icon { width: 24px; height: 20px; fill: var(--ink-slate); flex: none; }
</style>
</head>
<body>
<main class="canvas">

  <section class="card card-front" aria-label="Card front">
    <svg class="wave-art" viewBox="0 0 658 407" preserveAspectRatio="none" aria-hidden="true">
      <rect width="658" height="407" fill="var(--wave-grey)"/>
      <path d="M0,312 C110,372 210,372 320,305 C430,238 540,225 658,268 V407 H0 Z" fill="var(--paper)"/>
      <path d="M0,267 C100,330 190,345 300,298 C420,246 520,170 658,262 V0 H0 Z" fill="var(--navy)"/>
    </svg>
    <div class="brand">
      <span class="brand-dot"></span>
      <span class="brand-name">Quillmark Ledger</span>
    </div>
  </section>

  <section class="card card-back" aria-label="Card back">
    <div class="contact-frame"></div>
    <div class="person">
      <p class="person-name"><span class="first">Dana</span> <span class="last">Merrow</span></p>
      <p class="person-title">Founder/CEO</p>
    </div>
    <ul class="contact-list">
      <li class="contact-item">
        <svg class="contact-icon" viewBox="0 0 24 20" aria-hidden="true"><path d="M1 3h22v14H1z M2.5 4.5 12 11l9.5-6.5v1.6L12 12.6 2.5 6.1z" fill-rule="evenodd"/></svg>
        <span>dana@quillmarkledger.example</span>
      </li>
      <li class="contact-item">
        <svg class="contact-icon" viewBox="0 0 24 20" aria-hidden="true"><path d="M6 1c1 0 2 3 2.4 4.3.3 1-1.4 1.8-1.2 2.6.6 1.9 2.8 4.2 4.7 5 .8.3 1.6-1.4 2.6-1.1C15.8 12.2 19 13.3 19 14.3c0 1.5-1.6 3.7-3.4 3.7C9.2 18 2 10.8 2 4.4 2 2.6 4.5 1 6 1z"/></svg>
        <span>2740 Harlow Avenue, Boston MA 02135</span>
      </li>
      <li class="contact-item">
        <svg class="contact-icon" viewBox="0 0 24 20" aria-hidden="true"><path d="M12 1 1 10.5h3V19h6v-5.5h4V19h6v-8.5h3z"/></svg>
        <span>(617)555-0194</span>
      </li>
    </ul>
  </section>

</main>
</body>
</html>
```